Quarrel Ridge Advisory Business Card

Quarrel Ridge Advisory is a company that provides consulting services to the Mining Industry.

Whilst Quarrel Ridge Advisory is an Australian based company its client base is the global mining industry.

The essence of Quarrel Ridge Advisory is its a can do organisation that can make a difference to its clients by providing quality assistance and form lasting relationships.
Updates

Target Market(s)

The global Mining Industry.

Industry/Entity Type

Mining

Font styles to use
Serif

Colors

Designer to choose colors to be used in the design.

Requirements
Nice to have
• My thinking is the card would look good in black given the logo.

I would like to see written on the back side of the card " Providing Metallurgical, Management and Corporate Services to the Mining Industry"

```html
<!DOCTYPE html>
<html lang="en">
<head>
<meta charset="utf-8">
<title>Quarrel Ridge Advisory – Business Card</title>
<link href="https://fonts.googleapis.com/css2?family=Merriweather:ital,wght@0,300;0,400;0,700;1,300&display=swap" rel="stylesheet">
<style>
  :root {
    --backdrop: #e4e4e2;
    --card-black: #07030b;
    --card-white: #ffffff;
    --band: #07030b;
    --accent: #f0a01e;
    --ink: #1a1a1a;
    --ink-soft: #555555;
    --tagline: #d9d9d9;
  }
  * { box-sizing: border-box; margin: 0; padding: 0; }
  html, body {
    width: 1200px;
    height: 902px;
    overflow: hidden;
  }
  body {
    background: var(--backdrop);
    font-family: "Merriweather", serif;
    display: flex;
    align-items: center;
    justify-content: center;
    gap: 50px;
  }
  .card {
    width: 525px;
    height: 300px;
    position: relative;
    box-shadow: 0 6px 18px rgba(0,0,0,0.18);
    overflow: hidden;
  }

  /* Front */
  .card--front {
    background: var(--card-black);
    display: flex;
    flex-direction: column;
    align-items: center;
    justify-content: center;
    gap: 18px;
  }
  .brand {
    display: flex;
    align-items: center;
    gap: 8px;
    color: var(--accent);
    font-weight: 700;
    text-transform: uppercase;
    letter-spacing: 0.04em;
    white-space: nowrap;
  }
  .brand__square {
    width: 10px;
    height: 10px;
    background: var(--accent);
    flex: none;
  }
  .card--front .brand { font-size: 16px; }
  .tagline {
    max-width: 380px;
    text-align: center;
    color: var(--tagline);
    font-size: 10.5px;
    font-weight: 300;
    font-style: italic;
    line-height: 1.6;
    letter-spacing: 0.02em;
  }

  /* Back */
  .card--back { background: var(--card-white); }
  .card--back .brand {
    position: absolute;
    top: 26px;
    right: 30px;
    font-size: 11px;
  }
  .holder {
    position: absolute;
    left: 34px;
    top: 108px;
    color: var(--ink);
  }
  .holder__name {
    font-size: 24px;
    font-weight: 400;
    line-height: 1.1;
  }
  .holder__title {
    font-size: 12px;
    font-weight: 300;
    color: var(--ink-soft);
    margin-top: 3px;
  }
  .contact-band {
    position: absolute;
    left: 0;
    right: 0;
    top: 170px;
    height: 62px;
    background: var(--band);
    display: flex;
    align-items: center;
    justify-content: space-between;
    padding: 0 30px;
    list-style: none;
  }
  .contact-band li {
    color: var(--accent);
    font-size: 11px;
    font-weight: 300;
    white-space: nowrap;
  }
</style>
</head>
<body>
  <section class="card card--front" aria-label="Card front">
    <div class="brand"><span class="brand__square"></span>Quarrel Ridge Advisory</div>
    <p class="tagline">Providing Metallurgical, Management and Corporate Services to the Mining Industry</p>
  </section>

  <section class="card card--back" aria-label="Card back">
    <div class="brand"><span class="brand__square"></span>Quarrel Ridge Advisory</div>
    <div class="holder">
      <p class="holder__name">Name</p>
      <p class="holder__title">Title</p>
    </div>
    <ul class="contact-band">
      <li>xxx.xxx.xxxx</li>
      <li>email@email.com</li>
      <li>Address</li>
      <li>www.web.com</li>
    </ul>
  </section>
</body>
</html>
```